Plastic Business Card for Bookkeeper

We are looking for a simple professional business card design to use for printing on thin frosted plastic (see-through) card stock. Logo and brand guideline documents are attached as well as a photo of our old business card, and another business card example that we like.

Target Market(s)

Small Business

Industry/Entity Type

Bookkeeper

Contact Information for Business Card

Harriet Valdez CPA
Chief Executive Bookkeeper
T. 03 5926 4187
M. 0432 861 507
E. harriet@quillpathledger.com
W. www.quillpathledger.com

Font styles to use
Sans Serif

Colors
6b449b
00a990

Requirements
Must have
• Stick with logo colors. Writing should be clear and easy to read and not too cramped together.
Nice to have
• Tag line for back of the card - 'Not your ordinary Bookkeeper'

```html
<!DOCTYPE html>
<html lang="en">
<head>
<meta charset="utf-8">
<title>Harriet Valdez CPA – Business Card</title>
<link rel="stylesheet" href="https://fonts.googleapis.com/css2?family=Bebas+Neue&family=Montserrat:wght@600&family=Open+Sans:wght@400&display=swap">
<style>
  :root {
    --teal: #0b7a8c;
    --purple: #6c4ea0;
    --frost: #eef0f2;
    --disc: #f6f6f7;
    --white: #ffffff;
    --page: #e4e6e9;
  }
  * { margin: 0; padding: 0; box-sizing: border-box; }
  html, body { width: 1200px; height: 900px; overflow: hidden; background: var(--page); }
  .card {
    position: absolute; left: 150px; top: 171px;
    width: 900px; height: 558px;
    border-radius: 8px; overflow: hidden;
    box-shadow: 0 10px 30px rgba(0,0,0,.15);
  }
  .card-art { position: absolute; inset: 0; }
  .identity { position: absolute; left: 42px; top: 58px; color: var(--white); }
  .identity .name { font: 600 31px/1 "Montserrat", sans-serif; letter-spacing: .2px; }
  .identity .role { font: 400 22px/1 "Open Sans", sans-serif; margin-top: 8px; }
  .tagline { position: absolute; left: 42px; top: 188px; color: var(--purple); font-family: "Bebas Neue", sans-serif; line-height: 1; }
  .tagline span { display: block; font-size: 56px; margin-bottom: 12px; }
  .tagline .small { font-size: 43px; }
  .contacts { position: absolute; left: 42px; top: 408px; list-style: none; color: var(--white); font: 400 22px/1 "Open Sans", sans-serif; }
  .contacts li { display: flex; align-items: center; height: 33.5px; }
  .contacts svg { width: 18px; height: 18px; margin-right: 11px; fill: var(--white); }
  .brand { position: absolute; left: 436px; width: 400px; top: 238px; text-align: center; }
  .brand .dot { display: block; width: 46px; height: 46px; margin: 0 auto 26px; border-radius: 50%; background: var(--teal); }
  .brand .brand-name { font: 600 32px/1.3 "Montserrat", sans-serif; color: var(--purple); letter-spacing: 1px; }
</style>
</head>
<body>
<div class="card">
  <svg class="card-art" viewBox="0 0 900 558" width="900" height="558" aria-hidden="true">
    <defs>
      <filter id="disc-shadow" x="-20%" y="-20%" width="140%" height="140%">
        <feDropShadow dx="0" dy="2" stdDeviation="6" flood-opacity=".18"/>
      </filter>
    </defs>
    <rect width="900" height="558" fill="var(--frost)"/>
    <rect x="636" y="0" width="264" height="558" fill="var(--purple)"/>
    <polygon points="0,0 636,0 636,120 420,120 385,159 0,159" fill="var(--teal)"/>
    <polygon points="0,400 385,400 420,440 636,440 636,558 0,558" fill="var(--teal)"/>
    <circle cx="636" cy="278" r="255" fill="var(--disc)" filter="url(#disc-shadow)"/>
  </svg>

  <header class="identity">
    <h1 class="name">HARRIET VALDEZ CPA</h1>
    <p class="role">Chief Executive Bookkeeper</p>
  </header>

  <p class="tagline"><span>Not your</span><span>Ordinary</span><span class="small">Bookkeeper</span></p>

  <ul class="contacts">
    <li><svg viewBox="0 0 24 24"><path d="M3 8c0-3 4-4 9-4s9 1 9 4v2h-5V8H8v2H3zM6 11h12l2 9H4z"/></svg>03 5926 4187</li>
    <li><svg viewBox="0 0 24 24"><path d="M7 1h10a2 2 0 0 1 2 2v18a2 2 0 0 1-2 2H7a2 2 0 0 1-2-2V3a2 2 0 0 1 2-2zm0 3v14h10V4zm5 15.5a1.2 1.2 0 1 0 0 2.4 1.2 1.2 0 0 0 0-2.4z"/></svg>0432 861 507</li>
    <li><svg viewBox="0 0 24 24"><path d="M12 2a10 10 0 1 0 0 20 10 10 0 0 0 0-20zm-1 17.9A8 8 0 0 1 4.1 10L9 15v1a2 2 0 0 0 2 2zm6.9-2.5A2 2 0 0 0 16 16h-1v-3a1 1 0 0 0-1-1H8v-2h2a1 1 0 0 0 1-1V7h2a2 2 0 0 0 2-2v-.4a8 8 0 0 1 2.9 12.8z"/></svg>www.quillpathledger.com</li>
    <li><svg viewBox="0 0 24 24"><path d="M2 5h20v14H2zm2 2v.5l8 5 8-5V7zm0 2.8V17h16V9.8l-8 5z"/></svg>harriet@quillpathledger.com</li>
  </ul>

  <div class="brand">
    <span class="dot"></span>
    <p class="brand-name">QUILLPATH<br>LEDGER</p>
  </div>
</div>
</body>
</html>
```